Pelmar Scorecard

Redesign KTV's existing Pelmar scorecard, which tracks and reports key performance indicators (KPIs) for our clients. The scorecard provides our customers with an at-a-glance view of our on-site performance. Pelmar is a tool that automatically populates and reports this data.

Review the attached document and deliver suggested redesign options for the two attached views.
Page 1: Portfolio-wide views (high level rollup of multiple sites)
Page 2: Site-level view
Updates

Project Deadline Extended
Reason: Due to the holiday season within the U.S. around the globe we have decided to extend out deadline in hopes of gaining more participation. We will also be providing comments to the current designs tomorrow.

Font styles to use
Sans Serif

Requirements
Must have
• - Sans serif fonts
- Clean aesthetic
- Utilize the exact key performance indicators as are in the attached mockup
- White background (think Quince-esque)
Nice to have
• - Ideas for animation of design elements
Should not have
• - Pictures (icons are okay)

```html
<!DOCTYPE html>
<html lang="en">
<head>
<meta charset="utf-8">
<title>Pelmar Scorecard – All Sites</title>
<link rel="stylesheet" href="https://fonts.googleapis.com/css2?family=Open+Sans:wght@400;600;700&display=swap">
<style>
  :root{
    --orange:#f08a00;
    --brown:#b06a00;
    --green:#6fa312;
    --green-dark:#4d7a10;
    --ink:#4a4a4a;
    --muted:#777;
    --band:#e7e7e7;
    --band-edge:#d6d6d6;
    --grid:#d9d9d9;
    --axis:#555;
    --white:#fff;
  }
  *{box-sizing:border-box;margin:0;padding:0}
  html,body{width:1200px;height:996px;overflow:hidden;background:var(--white)}
  body{font-family:"Open Sans",Arial,sans-serif;color:var(--ink);position:relative}

  .masthead{position:absolute;left:0;top:0;width:1200px;height:135px}
  .brand{position:absolute;left:52px;top:40px;display:flex;align-items:center;gap:10px}
  .brand-dot{width:34px;height:34px;border-radius:50%;background:#8a8a8a}
  .brand-name{font-size:30px;font-weight:600;color:#8a8a8a;letter-spacing:-.5px}
  .page-title{position:absolute;left:282px;top:30px}
  .page-title h1{font-size:42px;font-weight:400;color:var(--orange);line-height:1.1}
  .page-title p{font-size:24px;color:var(--ink);line-height:1.3}
  .page-title strong{font-weight:700}
  .product{position:absolute;right:82px;top:70px;font-size:44px;color:var(--orange);line-height:1}
  .product span{font-size:27px;font-weight:700;color:var(--ink)}

  .nav-band{position:absolute;left:0;top:135px;width:1200px;height:243px;background:var(--band);border-top:1px solid var(--band-edge);border-bottom:1px solid var(--band-edge)}
  .nav-item{position:absolute;top:45px;width:130px;text-align:center}
  .nav-icon{width:90px;height:90px;border-radius:50%;background:var(--orange);margin:0 auto;display:flex;align-items:center;justify-content:center}
  .nav-item.active .nav-icon{background:var(--brown)}
  .nav-label{display:block;margin-top:9px;font-size:15px;font-weight:700;color:#666}
  .tab{position:absolute;top:176px;height:30px;background:var(--green);color:var(--white);font-size:15px;font-weight:700;display:flex;align-items:center;justify-content:center;border-radius:2px}
  .tab.active{background:var(--green-dark)}

  .chart{position:absolute;left:0;top:0}
  .chart text{font-family:"Open Sans",Arial,sans-serif}

  .summary{position:absolute;left:952px;top:496px}
  .summary h2{font-size:42px;font-weight:400;color:var(--orange);line-height:1}
  .summary .kpi{font-size:20px;font-weight:700;color:var(--ink);margin-top:6px}
  .summary .period{font-size:20px;color:var(--ink)}
  .site-score{position:absolute;left:960px;top:612px}
  .site-score h2{font-size:40px;font-weight:400;color:var(--orange);line-height:1}
  .site-score .goal{font-size:20px;font-weight:700;color:var(--ink);margin-top:4px}
  .score-dial{position:absolute;left:958px;top:700px;width:116px;height:116px;border-radius:50%;
    background:radial-gradient(circle at 40% 35%,#ffffff 0%,#e8e8e8 55%,#b9b9b9 100%);
    display:flex;align-items:center;justify-content:center;font-size:40px;font-weight:700;color:var(--green-dark)}

  .site-key{position:absolute;left:127px;top:851px;width:800px;font-size:11.5px;line-height:1.4;color:var(--ink)}
</style>
</head>
<body>

<header class="masthead">
  <div class="brand"><span class="brand-dot"></span><span class="brand-name">brenmoor</span></div>
  <div class="page-title">
    <h1>All Sites</h1>
    <p><strong>All Programs</strong> | July 2013</p>
  </div>
  <div class="product">KTV<span>Pelmar</span></div>
</header>

<nav class="nav-band">
  <div class="nav-item active" style="left:202px">
    <div class="nav-icon">
      <svg width="48" height="40" viewBox="0 0 48 40" fill="none" stroke="#fff" stroke-width="2">
        <rect x="2" y="2" width="14" height="10"/><rect x="32" y="2" width="14" height="10"/>
        <rect x="17" y="26" width="14" height="10"/><path d="M9 12v7h30v-7M24 19v7" stroke-dasharray="2 2"/>
      </svg>
    </div><span class="nav-label">Governance</span>
  </div>
  <div class="nav-item" style="left:365px">
    <div class="nav-icon">
      <svg width="48" height="42" viewBox="0 0 48 42" fill="none" stroke="#fff" stroke-width="2.5">
        <path d="M3 2v36h43"/><rect x="10" y="26" width="6" height="10" fill="#fff"/><rect x="20" y="20" width="6" height="16" fill="#fff"/><rect x="30" y="23" width="6" height="13" fill="#fff"/><path d="M8 20l10-8 8 5 16-13"/>
      </svg>
    </div><span class="nav-label">Cost</span>
  </div>
  <div class="nav-item" style="left:527px">
    <div class="nav-icon">
      <svg width="44" height="46" viewBox="0 0 44 46" fill="none" stroke="#fff" stroke-width="2.5">
        <path d="M12 3h18l10 10v30H12z"/><path d="M20 16h14M20 23h14M20 30h14"/><circle cx="9" cy="24" r="6" fill="#fff"/><path d="M5 29l-2 9 6-3 6 3-2-9"/>
      </svg>
    </div><span class="nav-label">Quality</span>
  </div>
  <div class="nav-item" style="left:690px">
    <div class="nav-icon">
      <svg width="40" height="46" viewBox="0 0 40 46" fill="#fff">
        <circle cx="20" cy="13" r="10"/><path d="M2 46c0-12 8-18 18-18s18 6 18 18z"/>
      </svg>
    </div><span class="nav-label">EHS</span>
  </div>
  <div class="nav-item" style="left:852px">
    <div class="nav-icon">
      <svg width="52" height="40" viewBox="0 0 52 40" fill="#fff">
        <circle cx="26" cy="10" r="8"/><circle cx="11" cy="14" r="6"/><circle cx="41" cy="14" r="6"/>
        <path d="M12 40c0-12 6-19 14-19s14 7 14 19z"/><path d="M0 36c0-9 5-14 11-14 2 0 3 .5 4 1-3 4-4 8-4 13z"/><path d="M52 36c0-9-5-14-11-14-2 0-3 .5-4 1 3 4 4 8 4 13z"/>
      </svg>
    </div><span class="nav-label">Personnel</span>
  </div>
  <div class="nav-item" style="left:1013px">
    <div class="nav-icon">
      <svg width="44" height="46" viewBox="0 0 44 46" fill="none" stroke="#fff" stroke-width="2.5">
        <path d="M6 3h24l8 8v16M6 3v38h16"/><path d="M12 14h16M12 21h16M12 28h8"/><path d="M38 26l-12 14-4 4 1-6 12-14z" fill="#fff"/>
      </svg>
    </div><span class="nav-label">Training</span>
  </div>

  <a class="tab active" style="left:219px;width:133px">Scorecard/KPIs</a>
  <a class="tab" style="left:360px;width:131px">Updates</a>
  <a class="tab" style="left:499px;width:134px">Innovations</a>
</nav>

<svg class="chart" width="940" height="840" viewBox="0 0 940 840" role="img" aria-label="KPI score by site, July 2013">
  <g stroke="var(--grid)" stroke-width="1" stroke-dasharray="2 2">
    <line x1="129" y1="493" x2="900" y2="493"/><line x1="129" y1="554" x2="900" y2="554"/>
    <line x1="129" y1="615" x2="900" y2="615"/><line x1="129" y1="675" x2="900" y2="675"/>
    <line x1="129" y1="736" x2="900" y2="736"/>
  </g>
  <g font-size="18" font-weight="700" fill="#555" text-anchor="end">
    <text x="122" y="500">100%</text><text x="116" y="561">90%</text><text x="116" y="622">80%</text>
    <text x="116" y="682">70%</text><text x="116" y="743">60%</text><text x="116" y="804">50%</text>
  </g>
  <g>
    <rect x="153" y="493" width="12" height="304" fill="var(--green)"/>
    <rect x="179" y="560" width="12" height="237" fill="var(--orange)"/>
    <rect x="206" y="572" width="12" height="225" fill="var(--green)"/>
    <rect x="232" y="493" width="12" height="304" fill="var(--orange)"/>
    <rect x="259" y="530" width="12" height="267" fill="var(--green)"/>
    <rect x="285" y="554" width="12" height="243" fill="var(--orange)"/>
    <rect x="312" y="493" width="12" height="304" fill="var(--green)"/>
    <rect x="338" y="554" width="12" height="243" fill="var(--orange)"/>
    <rect x="365" y="572" width="12" height="225" fill="var(--green)"/>
    <rect x="391" y="493" width="12" height="304" fill="var(--orange)"/>
    <rect x="418" y="530" width="12" height="267" fill="var(--green)"/>
    <rect x="444" y="554" width="12" height="243" fill="var(--orange)"/>
    <rect x="471" y="493" width="12" height="304" fill="var(--green)"/>
    <rect x="497" y="530" width="12" height="267" fill="var(--orange)"/>
    <rect x="524" y="554" width="12" height="243" fill="var(--green)"/>
    <rect x="550" y="493" width="12" height="304" fill="var(--orange)"/>
    <rect x="577" y="554" width="12" height="243" fill="var(--green)"/>
    <rect x="603" y="572" width="12" height="225" fill="var(--orange)"/>
    <rect x="630" y="493" width="12" height="304" fill="var(--green)"/>
    <rect x="656" y="530" width="12" height="267" fill="var(--orange)"/>
    <rect x="683" y="554" width="12" height="243" fill="var(--green)"/>
    <rect x="709" y="554" width="12" height="243" fill="var(--orange)"/>
    <rect x="736" y="493" width="12" height="304" fill="var(--green)"/>
    <rect x="762" y="554" width="12" height="243" fill="var(--orange)"/>
    <rect x="789" y="493" width="12" height="304" fill="var(--green)"/>
    <rect x="815" y="493" width="12" height="304" fill="var(--orange)"/>
    <rect x="842" y="530" width="12" height="267" fill="var(--green)"/>
    <rect x="868" y="554" width="12" height="243" fill="var(--orange)"/>
  </g>
  <line x1="129" y1="451" x2="129" y2="799" stroke="var(--axis)" stroke-width="4"/>
  <line x1="127" y1="797" x2="922" y2="797" stroke="var(--axis)" stroke-width="4"/>
  <g fill="#444" stroke="#fff" stroke-width="1">
    <circle cx="159" cy="797" r="9"/><circle cx="185" cy="797" r="9"/><circle cx="212" cy="797" r="9"/><circle cx="238" cy="797" r="9"/>
    <circle cx="265" cy="797" r="9"/><circle cx="291" cy="797" r="9"/><circle cx="318" cy="797" r="9"/><circle cx="344" cy="797" r="9"/>
    <circle cx="371" cy="797" r="9"/><circle cx="397" cy="797" r="9"/><circle cx="424" cy="797" r="9"/><circle cx="450" cy="797" r="9"/>
    <circle cx="477" cy="797" r="9"/><circle cx="503" cy="797" r="9"/><circle cx="530" cy="797" r="9"/><circle cx="556" cy="797" r="9"/>
    <circle cx="583" cy="797" r="9"/><circle cx="609" cy="797" r="9"/><circle cx="636" cy="797" r="9"/><circle cx="662" cy="797" r="9"/>
    <circle cx="689" cy="797" r="9"/><circle cx="715" cy="797" r="9"/><circle cx="742" cy="797" r="9"/><circle cx="768" cy="797" r="9"/>
    <circle cx="795" cy="797" r="9"/><circle cx="821" cy="797" r="9"/><circle cx="848" cy="797" r="9"/><circle cx="874" cy="797" r="9"/>
  </g>
  <g font-size="9" font-weight="700" fill="#fff" text-anchor="middle">
    <text x="159" y="800">1</text><text x="185" y="800">2</text><text x="212" y="800">3</text><text x="238" y="800">4</text>
    <text x="265" y="800">5</text><text x="291" y="800">6</text><text x="318" y="800">7</text><text x="344" y="800">8</text>
    <text x="371" y="800">9</text><text x="397" y="800">10</text><text x="424" y="800">11</text><text x="450" y="800">12</text>
    <text x="477" y="800">13</text><text x="503" y="800">14</text><text x="530" y="800">15</text><text x="556" y="800">16</text>
    <text x="583" y="800">17</text><text x="609" y="800">18</text><text x="636" y="800">19</text><text x="662" y="800">20</text>
    <text x="689" y="800">21</text><text x="715" y="800">22</text><text x="742" y="800">23</text><text x="768" y="800">24</text>
    <text x="795" y="800">25</text><text x="821" y="800">26</text><text x="848" y="800">27</text><text x="874" y="800">28</text>
  </g>
</svg>

<section class="summary">
  <h2>Scorecard</h2>
  <p class="kpi">KPI Score By Site</p>
  <p class="period">Showing July 2013</p>
</section>
<section class="site-score">
  <h2>Site Score</h2>
  <p class="goal">Goal 90%</p>
</section>
<div class="score-dial">86%</div>

<p class="site-key">1. Arlen - Menlo Park &nbsp;|&nbsp; 2. Velda - Vacaville &nbsp;|&nbsp; 3. ORB - Irvine &nbsp;|&nbsp; 4. Little Harbor - San Francisco &nbsp;|&nbsp; 5 TWK - Irwindale &nbsp;|&nbsp; 6. Halden - San Jose &nbsp;|&nbsp; 7. Homeward - Skillman &nbsp;|&nbsp; 8. Tessivan - Bridgewater &nbsp;|&nbsp; 9. Arlen - Menlo Park &nbsp;|&nbsp; 10 Velda - Vacaville &nbsp;|&nbsp; 11 ORB - Irvine &nbsp;|&nbsp; 12. Little Harbor - San Francisco &nbsp;|&nbsp; 13 TWK - Irwindale &nbsp;|&nbsp; 14. Halden - San Jose &nbsp;|&nbsp; 15. Homeward - Skillman &nbsp;|&nbsp; 16. Tessivan - Bridgewater &nbsp;|&nbsp; 17. Arlen - Menlo Park &nbsp;|&nbsp; 18. Velda - Vacaville &nbsp;|&nbsp; 19. ORB - Irvine &nbsp;|&nbsp; 20. Little Harbor - San Francisco &nbsp;|&nbsp; 22. TWK - Irwindale &nbsp;|&nbsp; 23. Halden - San Jose &nbsp;|&nbsp; 24. Homeward - Skillman &nbsp;|&nbsp; 25. Tessivan - Bridgewater &nbsp;|&nbsp; 26. Halden - San Jose &nbsp;|&nbsp; 27. Homeward - Skillman &nbsp;|&nbsp; 28. Tessivan - Bridgewater</p>

</body>
</html>
```